Brocure for Brindle - Social Media Management

Brindle is a Dutch company in the market of Social Media growth. We need a brochure (digital/PDF) for our company. Please see attached word doc for the text and attached logo. The initial proposal can contain just the first 4 pages text of the word doc.

We use informal language in all our communication.

Slogan: Effectieve Social Media Marketing voor professionals en ondernemers

Website: brindlesm-voorbeeld.nl

Industry/Entity Type

Digital Marketing

Contact Information for Business Card

Contact details:

Gerrit ter Hoeve
gerrit@brindlesm-voorbeeld.nl
06-19573826

```html
<!DOCTYPE html>
<html lang="nl">
<head>
<meta charset="utf-8">
<title>Brindle – brochure</title>
<link rel="stylesheet" href="https://fonts.googleapis.com/css2?family=Montserrat:wght@300;400;500;600;700;800&family=Oswald:wght@500&display=swap">
<style>
:root{
  --orange:#ec6a24;
  --navy:#232c44;
  --ink:#2b2b2b;
  --body:#5c5c5c;
  --grey-cell:#e9e9eb;
  --bg-top:#8c8c8c;
  --bg-bottom:#262626;
}
*{box-sizing:border-box;margin:0;padding:0}
html,body{width:1200px;height:2194px;overflow:hidden}
body{background:linear-gradient(180deg,var(--bg-top),var(--bg-bottom));font-family:"Montserrat",sans-serif;position:relative}
.page{position:absolute;width:494px;height:640px;background:#fff;overflow:hidden}
.page--edge{border-bottom:3px solid var(--orange)}
.p1{left:82px;top:88px}.p2{left:624px;top:88px}
.p3{left:82px;top:779px}.p4{left:624px;top:779px}
.p5{left:82px;top:1471px}

.section-title{color:var(--orange);font-weight:700;font-size:19px;line-height:1;border-left:2px solid var(--orange);padding-left:14px;margin-left:42px;letter-spacing:.1px;white-space:nowrap}
.copy{margin:0 42px;color:var(--body);font-size:6.3px;line-height:1.38;font-weight:400}
.copy p{margin-top:4px}

/* cover */
.cover-logo{position:absolute;left:176px;top:48px;display:flex;align-items:center;gap:12px}
.logo-dot{width:54px;height:54px;border-radius:50%;background:var(--orange)}
.logo-name{font-weight:800;color:var(--orange);font-size:34px;letter-spacing:1px;white-space:nowrap}
.cover-photo{position:absolute;left:0;top:144px;width:494px;height:352px;background:linear-gradient(120deg,#5a3328 0%,#243a4a 38%,#1f2a3a 65%,#0f1722 100%)}
.cover-headline{position:absolute;left:53px;top:232px;font-weight:800;line-height:1.04}
.cover-headline .hl-orange{color:var(--orange);font-size:27px}
.cover-headline .hl-white{color:#fff;font-size:24px}
.cover-rule{position:absolute;left:0;top:600px;width:250px;height:1.5px;background:var(--orange)}
.cover-url{position:absolute;right:46px;top:594px;font-size:10px;letter-spacing:1.6px;color:#444;white-space:nowrap}
.cover-url b{color:var(--orange);font-weight:700}

/* page 2 */
.intro-band{position:absolute;left:0;top:0;width:494px;height:167px;background:var(--orange);color:#fff}
.intro-title{position:absolute;left:44px;top:28px;border-left:2px solid #fff;padding-left:14px;font-weight:700;font-size:18.5px;line-height:1.3}
.intro-sub{position:absolute;left:58px;top:88px;font-size:10.5px;font-weight:500}
.intro-text{position:absolute;left:42px;top:108px;width:410px;font-size:6.2px;line-height:1.45;font-weight:300}
.intro-text p{margin-bottom:3px}
.formula{position:absolute;left:42px;top:153px;width:410px;height:27px;background:var(--navy);color:#fff;font-family:"Oswald",sans-serif;font-size:11.5px;display:flex;align-items:center;justify-content:center;letter-spacing:.2px}
.illus{position:absolute;border-radius:6px}
.platform-list{position:absolute;left:42px;top:548px;width:420px;display:grid;grid-template-columns:240px 180px;row-gap:7px}
.platform{display:flex;gap:8px;align-items:flex-start;font-size:7.4px;color:var(--ink);font-weight:600;line-height:1.25}
.platform .dot{width:17px;height:17px;border-radius:50%;background:var(--navy);flex:none}
.platform .dot.small{width:11px;height:11px;margin-top:1px;background:var(--orange)}
.platform b{color:var(--orange);display:block}

/* page 3 */
.top-strip{position:absolute;left:42px;top:0;width:452px;height:3px;background:var(--navy)}
.work-band{position:absolute;left:0;top:288px;width:494px;height:236px;background:var(--orange)}
.work-band::before{content:"";position:absolute;left:0;top:0;width:42px;height:100%;background:var(--navy)}
.work-cols{position:absolute;left:62px;top:13px;width:400px;display:grid;grid-template-columns:1fr 1fr;column-gap:18px;color:#fff}
.step h4{font-size:9px;font-weight:500;margin:0 0 3px}
.step h4::before{content:"✓";display:inline-block;width:9px;height:9px;border:1px solid #fff;border-radius:50%;font-size:6px;text-align:center;line-height:8px;margin-right:4px;vertical-align:1px}
.step p{font-size:5.7px;line-height:1.4;font-weight:300;text-align:justify;margin-bottom:4px;opacity:.92}
.step{margin-bottom:6px}
.contact-tab{position:absolute;left:42px;top:539px;height:20px;width:192px;background:var(--navy);color:#fff;font-size:10px;font-weight:600;padding:4px 0 0 19px;clip-path:polygon(0 0,92% 0,100% 100%,0 100%)}
.contact-rule{position:absolute;left:42px;top:558px;width:410px;height:1.5px;background:var(--navy)}
.social-dots{position:absolute;left:389px;top:542px;display:flex;gap:3px}
.social-dots span{width:13px;height:13px;border-radius:50%;background:var(--navy)}
.contact-lines{position:absolute;left:47px;top:568px;font-size:8.6px;color:var(--ink);font-weight:500;line-height:1.95;white-space:nowrap}
.contact-lines i{display:inline-block;width:6px;height:6px;border-radius:50%;background:var(--orange);margin-right:6px;vertical-align:0}
.foot-logo{position:absolute;left:326px;top:576px;display:flex;align-items:center;gap:8px}
.foot-logo .logo-dot{width:34px;height:34px}
.foot-logo .logo-name{font-size:20px}

/* page 4 */
.growth-band{position:absolute;left:0;top:333px;width:494px;height:190px;background:var(--orange)}
.growth-text{position:absolute;left:0;top:0;width:262px;height:190px;background:var(--navy);color:#fff;padding:18px 18px 0 42px;font-size:6.3px;line-height:1.4;font-weight:300;text-align:justify}
.growth-text p{margin-bottom:7px}

/* page 5 */
.services{position:absolute;left:42px;top:90px;width:410px;border-collapse:separate;border-spacing:0 2px;font-size:7.4px;color:var(--ink)}
.services th{font-weight:500;color:#fff;background:var(--orange);font-size:6.6px;line-height:1.1;padding:4px 0 3px;width:31.6px;text-align:center}
.services th .hd{display:block;width:9px;height:9px;border-radius:50%;background:var(--navy);margin:0 auto 3px}
.services th.blank{background:var(--grey-cell);width:126px}
.services td{height:15.5px;text-align:center;border-left:1px solid #fff;background:#fff;box-shadow:inset 0 -1px 0 #e2e2e2;color:var(--orange);font-size:10px;line-height:1}
.services td.label{text-align:left;padding-left:9px;color:var(--ink);font-size:7.4px;background:#f1f1f2;border-left:0}
.services tr.group td{background:var(--grey-cell);box-shadow:none}
.services tr.group td.label{background:var(--orange);color:#fff;font-weight:600;font-size:8.2px}
.footnote{position:absolute;left:42px;top:521px;font-size:6.2px;color:var(--ink);font-weight:500}
</style>
</head>
<body>

<!-- Cover -->
<section class="page p1">
  <div class="cover-photo" role="img" aria-label="Foto: man die lachend naar een tablet kijkt, stapel app-tegels en laptop met statistieken"></div>
  <div class="cover-logo"><span class="logo-dot"></span><span class="logo-name">BRINDLE</span></div>
  <h1 class="cover-headline">
    <span class="hl-orange">Laat de<br>groei van je<br>sociale</span><br>
    <span class="hl-white">netwerken<br>over aan de<br>professionals!</span>
  </h1>
  <div class="cover-rule"></div>
  <div class="cover-url">www.<b>brindlesm-voorbeeld</b>.nl</div>
</section>

<!-- Intro / platforms -->
<section class="page p2 page--edge">
  <div class="intro-band">
    <h2 class="intro-title">Social Media Marketing voor<br>zakelijke professionals en ondernemers</h2>
    <div class="intro-sub">Groei, interactie en content</div>
    <div class="intro-text">
      <p>Je bereik vergroten, traffic genereren en daarmee meer omzet behalen. Dat is wat wij bieden.</p>
      <p>Onze services helpen jouw bereik op de sociale media te vergroten. Met een uitgekiende groeistrategie, onze kennis en geavanceerde tools zorgen we voor gerichte content en interactie op je sociale netwerken.</p>
    </div>
  </div>
  <div class="formula">((actieve interactie + relevante content) &gt; actieve volgers) = (&gt; traffic + omzet)</div>

  <div style="position:absolute;top:197px;left:0;width:240px">
    <h3 class="section-title">Wie zijn wij?</h3>
    <div class="copy" style="margin-top:8px;margin-right:0">
      <p>Wij zijn Brindle. Een team van sociale media experts dat je sociale netwerk activeert en het bereik vergroot. We zorgen voor sociale interactie met volgers, nieuwe en bestaande. Daarmee genereren we traffic naar je website/shop.</p>
      <p>Het doel? Meer omzet. Simpel en heel meetbaar.</p>
    </div>
  </div>
  <div class="illus" style="left:275px;top:198px;width:170px;height:150px;background:radial-gradient(circle at 50% 50%,#e6effa,#f6f9fd 70%,#fff)" role="img" aria-label="Illustratie: hand met smartphone omringd door zwevende sociale iconen"></div>

  <div style="position:absolute;top:290px;left:0;width:250px">
    <h3 class="section-title">Voor wie?</h3>
    <div class="copy" style="margin-top:8px;margin-right:0">
      <p>Onze dienstverlening kan ingezet worden op zowel persoonlijke zakelijke profielen (bv Vakkring), of voor bedrijfspagina's op diverse sociale mediakanalen.</p>
    </div>
  </div>

  <div style="position:absolute;top:357px;left:0;width:494px">
    <h3 class="section-title">Wat doen we?</h3>
    <div class="copy" style="margin-top:8px">
      <p>Samen met jou bepalen we je doelen in de sociale netwerken. Zowel strategisch als tactisch en operationeel. Wij richten ons op die doelen en zorgen voor een netwerk van echte en actieve volgers.</p>
      <p>Of het nu gaat om Vakkring, Fotostroom, Buurtplein of Kwetter, interactie zorgt voor betrokken volgers. Die jij vervolgens in je verkoopproces kunt oppakken.</p>
      <p>Voor zakelijke professionals verzorgen wij personal branding met als doel impact en social sales. We zorgen voor veel meer relevante connecties en activeren je zakelijke netwerk. Gecombineerd met de juiste contentstrategie, zorgen wij ervoor dat je gezien wordt als autoriteit in je vakgebied.</p>
      <p>Onze diensten voor bedrijven bestaan uit de versnelde organische groei van het volgernetwerk, het activeren van het netwerk met content en interactie. We zorgen daarmee voor een groot bereik en verkeer naar je website.</p>
    </div>
  </div>

  <h3 class="section-title" style="position:absolute;top:503px">Welke platformen?</h3>
  <div style="position:absolute;left:58px;top:528px;font-size:9.5px;font-weight:500;color:var(--ink)">We bieden onze diensten aan op alle belangrijke platformen:</div>
  <div class="platform-list">
    <div class="platform"><span class="dot"></span><span><b>Vakkring</b>(bedrijfspagina's en persoonlijke profielen)</span></div>
    <div class="platform"><span class="dot small"></span><span><b>Kwetter</b></span></div>
    <div class="platform"><span class="dot"></span><span><b>Buurtplein</b>(bedrijfspagina's en groepen)</span></div>
    <div class="platform"><span class="dot small"></span><span><b>Kijkkanaal</b><b>Zaakwijzer</b></span></div>
    <div class="platform"><span class="dot"></span><span><b>Fotostroom</b>(bedrijfspagina's en persoonlijke profielen)</span></div>
    <div class="platform"><span class="dot small"></span><span>Optioneel:<br>Dansclip, Prikwand, Praatplein en Blogrol</span></div>
  </div>
</section>

<!-- Network / how it works -->
<section class="page p3 page--edge">
  <div class="top-strip"></div>
  <h3 class="section-title" style="margin-top:30px">Activeren van je netwerk</h3>
  <div class="copy" style="margin-top:7px">
    <p>Je bent al een poos bezig met het beheren van je sociale media, maar ziet geen commercieel resultaat? De specialist maakt het verschil. Jouw kennis van jouw product en klant, gecombineerd met ons specialisme over sociale media. In zeer diverse branches.</p>
    <p>Wij gebruiken deze kennis voor een contentstrategie op maat. Een strategie die gegarandeerd meer likes, retweets en doorklikks genereert. Meer likes, meer interactie, meer betrokkenheid: meer omzet.</p>
  </div>
  <h3 class="section-title" style="margin-top:26px">Groeistrategie</h3>
  <div class="copy" style="margin-top:8px">
    <p>Je netwerk op sociale media laten groeien kan een lastige klus zijn. Maar het levert je enorm veel op. Een groot aantal echte en actieve volgers geeft vertrouwen en genereert nog meer betrokkenheid. Het is de moderne variant van mond-tot-mondreclame.</p>
    <p>Wij hebben de expertise en oplossingen om al je profielen een echte boost te geven. Met onze tools krijgen we de volledige controle over je kanalen, zodat jij jouw focus kunt richten op de uitvoering en levering van opdrachten.</p>
    <p>En wees voorbereid op groei!</p>
  </div>
  <h3 class="section-title" style="position:absolute;top:268px">Hoe werkt het?</h3>
  <div class="work-band">
    <div class="work-cols">
      <div>
        <div class="step"><h4>Quick Scan &amp; advies</h4><p>We starten altijd met een grondige analyse van je website en sociale kanalen. Op basis daarvan geven we je een advies over de beste strategie.</p></div>
        <div class="step"><h4>Pakketkeuze</h4><p>We hebben verschillende servicepakketten waaruit je kunt kiezen wat bij jouw situatie en wensen past. Blijkt op basis van de Quick Scan dat je beter af bent met maatwerk, dan maken we daarover specifieke afspraken.</p><p>Geen twee klanten zijn gelijk, daarom is ons aanbod flexibel opgebouwd.</p></div>
        <div class="step"><h4>Terugkoppeling en verbetering</h4><p>Iedere ondernemer is gedreven als het gaat om het behalen van resultaten. Zo ook wij. Wij doen er alles aan om onze dienstverlening zo succesvol mogelijk te laten zijn en jouw sociale doelen te behalen. We hebben regelmatig contact om de resultaten te bespreken en daar waar mogelijk te verbeteren.</p></div>
      </div>
      <div>
        <div class="step"><h4>Je wilt met ons in zee</h4><p>Als je besluit met ons in zee te gaan, doen we dat niet voor een paar weken. Want we doen niet aan hit- and run, maar bouwen aan samenwerking die op de lange termijn echte resultaten oplevert. We moeten elkaar goed leren kennen en dat vraagt tijd.</p><p>Je vertrouwt ons je sociale mediakanalen toe. Dat vraagt vertrouwen en tegelijk moeten wij ons goed inleven in de manier van communicatie die past bij jouw business en jouw doelgroep. Van beide kanten vraagt dit een tijdsinvestering.</p></div>
        <div class="step"><h4>Implementatie</h4><p>Natuurlijk wil je zo snel mogelijk resultaat zien. Dat willen wij ook. We werken de strategie uit in een plan en gaan voor jou aan het werk. Met de prioriteit op die gebieden die zo snel mogelijk resultaten opleveren. Omdat we graag (laten) zien dat onze inspanningen verschil maken.</p><p>We richten daarvoor de benodigde systemen in. In het begin hebben we regelmatig overleg om elkaar goed te leren kennen en de vinger aan de pols te houden.</p></div>
      </div>
    </div>
  </div>
  <div class="contact-tab">NEEM DAN CONTACT OP</div>
  <div class="contact-rule"></div>
  <div class="social-dots"><span></span><span></span><span></span><span></span></div>
  <div class="contact-lines">
    <div><i></i>Lindeweg 8, 6711 AA Ede</div>
    <div><i></i>info@brindlesm-voorbeeld.nl<i style="margin-left:8px"></i>06-19573826</div>
    <div><i></i>www.brindlesm-voorbeeld.nl</div>
  </div>
  <div class="foot-logo"><span class="logo-dot"></span><span class="logo-name">BRINDLE</span></div>
</section>

<!-- Why us -->
<section class="page p4 page--edge">
  <h3 class="section-title" style="margin-top:30px">Waarom kies je voor ons?</h3>
  <div class="copy" style="margin-top:8px">
    <p>Jij hebt jouw vak, wij het onze. Als iedereen doet waar hij goed in is, worden daar allemaal beter van. Wij zijn goed in het activeren en vergroten van je sociale netwerk. Daarvoor gebruiken we een slimme mix van kennis en tools.</p>
    <p>Een strategie die ervoor zorgt dat jij je kunt focussen op je corebusiness. Met onze slimme tools vergroten wij de impact van je sociale netwerken. Met als resultaat: meer traffic, meer leads, meer omzet.</p>
  </div>
  <h3 class="section-title" style="margin-top:20px">Doen we alles zelf?</h3>
  <div class="copy" style="margin-top:8px;text-align:justify">
    <p>Wij zijn slim in de strategie en systemen voor het vergroten van interactie. En we hebben een netwerk van specialisten die slim zijn in hun vak. Zoals een reclamebureau, creatief ontwerper, websitebouwer of marketingstrategiebureau.</p>
    <p>Is er op dat vlak een behoefte, dan brengen wij je graag in contact.</p>
  </div>
  <h3 class="section-title" style="margin-top:20px">Hoe lang gaan we met elkaar in zee?</h3>
  <div class="copy" style="margin-top:8px">
    <p>Een groeistrategie werkt op de lange termijn het beste als de groei organisch is. En dat vraagt dus ook een strategie voor de lange termijn. Lang is relatief, maar je moet erop rekenen dat we minimaal een jaar nodig hebben om de groeistrategie optimaal te laten werken.</p>
    <p>Natuurlijk is er in elke situatie snelle winst te behalen. Maar voor een goede samenwerking is het belangrijk dat je elkaar leert kennen en begrijpen. Daarom vragen we ook regelmatig jouw energie en input.</p>
  </div>
  <h3 class="section-title" style="position:absolute;top:313px">Groeien op sociale media</h3>
  <div class="growth-band">
    <div class="growth-text">
      <p>Het staat als een paal boven water: sociale media zijn een krachtig marketinginstrument. Een kans die je niet voorbij kunt laten gaan, of je dat nou leuk vindt of niet. Het geeft je de kans om je merk op te bouwen, je zicht- en vindbaarheid te verbeteren en uiteindelijk meer leads en verkopen te genereren.</p>
      <p>Het beheren van je sociale platforms is een tijdrovende klus. En om resultaat te krijgen, moet je het ook nog eens slim doen. Om de online herkenbaarheid van je bedrijf te vergroten, zijn je uitingen de sleutel.</p>
      <p>Interactie, consistentie, responsiveness, allemaal zorgen ze voor herkenning en betrokkenheid van je volgers. We helpen je om je digitale activiteiten met elkaar te verbinden en je bedrijf te laten groeien.</p>
    </div>
    <div style="position:absolute;left:262px;top:0;width:188px;height:190px;background:linear-gradient(135deg,#3f6fe0,#2a4fc0 60%,#6d8ff0)" role="img" aria-label="Illustratie: hand met magneet die volgers en likes aantrekt"></div>
  </div>
  <h3 class="section-title" style="position:absolute;top:542px">Volledig sociaal management</h3>
  <div class="copy" style="position:absolute;top:568px">
    <p>We bieden een compleet beheerpakket voor sociale media waarmee we betrokkenheid van volgers realiseren en tijdig en altijd proactief schakelen naar de volgende stap. Zo blijven bezoekers geboeid en actief.</p>
    <p>We plannen zowel doelgroep- als branche specifieke inhoud en combineren online aanwezigheid om meer en meer gericht websiteverkeer te genereren.</p>
  </div>
</section>

<!-- Services table -->
<section class="page p5 page--edge">
  <h3 class="section-title" style="margin-top:30px">Wat doen wij:</h3>
  <div style="position:absolute;left:42px;top:64px;font-size:6.6px;font-weight:600;color:var(--ink)">Zie onderstaand overzicht met onze diensten en services, onder het overzicht beschrijven we de mogelijkheden.</div>
  <table class="services">
    <thead>
      <tr>
        <th class="blank"></th>
        <th><span class="hd"></span>VK<br>Page</th><th><span class="hd"></span>VK<br>Profile</th><th><span class="hd"></span>BP<br>Page</th><th><span class="hd"></span>BP<br>Groep</th><th><span class="hd"></span>BP<br>Profile</th><th><span class="hd"></span>FS<br>Page</th><th><span class="hd"></span>KW<br>Page</th><th><span class="hd"></span>KK<br>Page</th><th><span class="hd"></span>ZW<br>Page</th>
      </tr>
    </thead>
    <tbody>
      <tr class="group"><td class="label">Geagendeerd posten</td><td></td><td></td><td></td><td></td><td></td><td></td><td></td><td></td><td></td></tr>
      <tr><td class="label">Tekst/Foto posts</td><td>✓</td><td>✓</td><td>✓</td><td>✓</td><td></td><td>✓</td><td>✓</td><td>✓</td><td>✓</td></tr>
      <tr><td class="label">Tekst/Video posts</td><td>✓</td><td>✓</td><td>✓</td><td>✓</td><td></td><td>✓</td><td>✓</td><td>✓</td><td></td></tr>
      <tr class="group"><td class="label">Groei Netwerk</td><td></td><td></td><td></td><td></td><td></td><td></td><td></td><td></td><td></td></tr>
      <tr><td class="label">Volgen en ontvolgen</td><td></td><td></td><td></td><td>✓</td><td></td><td>✓</td><td>✓</td><td>✓</td><td></td></tr>
      <tr><td class="label">Vrienden/Connecties</td><td></td><td>✓</td><td></td><td></td><td>✓</td><td></td><td></td><td></td><td></td></tr>
      <tr class="group"><td class="label">Interactie</td><td></td><td></td><td></td><td></td><td></td><td></td><td></td><td></td><td></td></tr>
      <tr><td class="label">Posts Likes</td><td>✓</td><td>✓</td><td>✓</td><td>✓</td><td>✓</td><td>✓</td><td>✓</td><td>✓</td><td></td></tr>
      <tr><td class="label">Comments</td><td></td><td>✓</td><td>✓</td><td>✓</td><td>✓</td><td>✓</td><td>✓</td><td>✓</td><td></td></tr>
      <tr class="group"><td class="label">Berichten</td><td></td><td></td><td></td><td></td><td></td><td></td><td></td><td></td><td></td></tr>
      <tr><td class="label">Mailing/bulk</td><td></td><td>✓</td><td></td><td>✓</td><td>✓</td><td>✓</td><td>✓</td><td>✓</td><td></td></tr>
      <tr><td class="label">Auto antwoord</td><td></td><td>✓</td><td></td><td>✓</td><td>✓</td><td>✓</td><td>✓</td><td>✓</td><td></td></tr>
      <tr class="group"><td class="label">Diversen</td><td></td><td></td><td></td><td></td><td></td><td></td><td></td><td></td><td></td></tr>
      <tr><td class="label">Datamining</td><td>✓</td><td>✓</td><td>✓</td><td>✓</td><td>✓</td><td>✓</td><td>✓</td><td>✓</td><td></td></tr>
      <tr><td class="label">Onderschrijven</td><td></td><td>✓</td><td></td><td></td><td></td><td></td><td></td><td></td><td></td></tr>
      <tr><td class="label">Uitnodigen pagina's</td><td></td><td>✓</td><td></td><td></td><td>✓</td><td>✓</td><td>✓</td><td>✓</td><td></td></tr>
      <tr><td class="label">Analyse en rapportage</td><td>✓</td><td>✓</td><td>✓</td><td>✓</td><td>✓</td><td>✓</td><td>✓</td><td>✓</td><td>✓</td></tr>
      <tr><td class="label">Content management</td><td>✓</td><td>✓</td><td>✓</td><td>✓</td><td>✓</td><td>✓</td><td>✓</td><td>✓</td><td>✓</td></tr>
      <tr><td class="label">SEO</td><td>✓</td><td>✓</td><td>✓</td><td>✓</td><td>✓</td><td>✓</td><td>✓</td><td>✓</td><td>✓</td></tr>
      <tr><td class="label">SEA</td><td>✓</td><td></td><td>✓</td><td>✓</td><td></td><td>✓</td><td>✓</td><td>✓</td><td></td></tr>
      <tr><td class="label">Monitoring</td><td>✓</td><td></td><td>✓</td><td>✓</td><td></td><td>✓</td><td>✓</td><td>✓</td><td></td></tr>
    </tbody>
  </table>
  <div class="footnote">*Optioneel bieden wij diensten op Prikwand, Blogrol en Praatplein aan.</div>
  <h3 class="section-title" style="position:absolute;top:541px">Geagendeerd posten</h3>
  <div class="copy" style="position:absolute;top:566px">
    <p>Geagendeerd posten is meer dan de voorbereiding van posts, het kiezen van de juiste hashtags en het redigeren van teksten. Per platform worden andere formaten van foto's en video's gevraagd. Wij zorgen ervoor dat ze voor ieder platform het juiste formaat hebben.</p>
    <p>Daarnaast analyseren wij de posts en doelgroepen zodat we de berichten op het juiste moment van de dag plaatsen, voor het meeste effect en de meeste interactie met de doelgroep.</p>
  </div>
</section>

</body>
</html>
```